Word document template for sales proposals

I am after a template that is simple but impactful. Use of colour to be limited but some for impact would be good. The proposals are for use in the professional technical field.

```html
<!DOCTYPE html>
<html lang="en">
<head>
<meta charset="utf-8">
<title>Proposal Cover – Clearflow Solutions</title>
<link rel="stylesheet" href="https://fonts.googleapis.com/css2?family=Barlow:wght@400;500;700&display=swap">
<style>
  :root {
    --orange: #f7941d;
    --blue: #29a9e1;
    --ink: #111111;
    --rule: #333333;
    --paper: #ffffff;
  }
  * { margin: 0; padding: 0; box-sizing: border-box; }
  html, body {
    width: 1200px;
    height: 1199px;
    overflow: hidden;
    background: var(--paper);
  }
  .cover {
    position: relative;
    width: 1200px;
    height: 1199px;
    font-family: "Barlow", sans-serif;
    color: var(--ink);
  }
  .brand {
    position: absolute;
    left: 258px;
    top: 494px;
    width: 280px;
    text-align: center;
  }
  .brand-mark {
    display: block;
    margin: 0 auto 22px;
  }
  .brand-name {
    font-weight: 700;
    font-size: 23px;
    letter-spacing: 0.5px;
    color: var(--orange);
    text-transform: uppercase;
    line-height: 1;
    white-space: nowrap;
  }
  .divider {
    position: absolute;
    left: 589px;
    top: 364px;
    width: 1px;
    height: 508px;
    background: var(--rule);
  }
  .contact {
    position: absolute;
    left: 647px;
  }
  .contact.prepared-by { top: 450px; }
  .contact.prepared-for { top: 658px; }
  .contact-label {
    font-weight: 500;
    font-size: 25px;
    line-height: 28px;
    color: var(--orange);
    text-transform: uppercase;
  }
  .contact-label .lower { text-transform: none; }
  .prepared-by .contact-label { margin-bottom: 24px; }
  .prepared-for .contact-label { margin-bottom: 11px; }
  .contact-name {
    font-weight: 700;
    font-size: 24px;
    line-height: 26px;
  }
  .contact-line {
    font-weight: 500;
    font-size: 19.5px;
    line-height: 22.7px;
    letter-spacing: 0.3px;
    white-space: nowrap;
  }
</style>
</head>
<body>
<main class="cover">
  <div class="brand">
    <svg class="brand-mark" width="88" height="88" viewBox="0 0 88 88" aria-hidden="true">
      <circle cx="44" cy="44" r="44" fill="var(--blue)"/>
    </svg>
    <div class="brand-name">Clearflow Solutions</div>
  </div>

  <div class="divider"></div>

  <section class="contact prepared-by">
    <h2 class="contact-label">Prepared By:</h2>
    <p class="contact-name">Mr ABC</p>
    <p class="contact-line">Bussiness Development Manager</p>
    <p class="contact-line">(5550100234)</p>
    <p class="contact-line">mr.abc@clearflow.example</p>
  </section>

  <section class="contact prepared-for">
    <h2 class="contact-label">Prepared <span class="lower">For:</span></h2>
    <p class="contact-name">Mr ABC</p>
    <p class="contact-line">Bussiness Development Manager</p>
    <p class="contact-line">(5550100234)</p>
    <p class="contact-line">mr.abc@clearflow.example</p>
  </section>
</main>
</body>
</html>
```